LoanCrest Mortgage Business Cards

We are a relatively new mortgage company, and we need business cards. We'd like a modern design. We want our business cards to grab attention without being too dramatic or presumptuous.
Our name: LoanCrest Mortgage. Our logos in horizontal and vertical executions are attached.
Our contact info:
6120 Amber Heron Blvd, Suite 415
Las Vegas, NV 89147
702-514-7390
We need the following disclaimer:
©2017 A division of Harborline Lending Mortgage LLC | Equal Housing Lender | NMLS ID # 5382 | Mortgage Banker License #0627539 | Licensed by the Department of Business Oversight under the Pacific Home Loan Conduct Act
We would like an option with and an option without a photo of the employee. For the design let's use this info:
Dana Morrow, MBA
Director
NMLS # 846215
Direct Office: (702) 514-7381
Cell: (702) 926-1847
Fax: (844) 637-2186
dana.morrow@lcmhome.com
Dana's photo is attached.
We'd like a double-sided card. It might be interesting to use our brand red (#f40000) on the back. As a thought starter, see attached for how our customer letters look.
Standard size. See description for brief.

```html
<!DOCTYPE html>
<html lang="en">
<head>
<meta charset="utf-8">
<title>LoanCrest Mortgage Business Cards</title>
<link href="https://fonts.googleapis.com/css2?family=Roboto+Condensed:wght@300;400;700&display=swap" rel="stylesheet">
<style>
  :root{
    --bg:#1a1a1a;
    --brand-red:#e8202d;
    --brand-red-dark:#c9111d;
    --ink:#3b3b3b;
    --paper:#f4f4f4;
    --divider:#111111;
    --white:#ffffff;
  }
  *{margin:0;padding:0;box-sizing:border-box}
  html,body{width:848px;height:1200px;overflow:hidden;background:var(--bg)}
  body{font-family:"Roboto Condensed",Arial,sans-serif;position:relative}
  .card{
    position:absolute;left:104px;width:640px;height:366px;border-radius:26px;overflow:hidden;
    box-shadow:0 18px 40px rgba(0,0,0,.55);
  }
  .card--front{top:170px;background:linear-gradient(150deg,var(--brand-red) 0%,var(--brand-red-dark) 100%)}
  .card--back{top:664px;display:flex}
  .brand{display:flex;align-items:center;gap:14px}
  .brand__dot{width:30px;height:30px;border-radius:50%;background:var(--ink)}
  .brand__name{font-weight:700;color:var(--ink);letter-spacing:.5px}
  .card--front .brand{position:absolute;left:50%;top:50%;transform:translate(-50%,-50%)}
  .card--front .brand__name{font-size:52px}
  .back__logo-side{width:250px;background:var(--paper);display:flex;align-items:center;justify-content:center}
  .back__logo-side .brand{gap:10px}
  .back__logo-side .brand__dot{width:20px;height:20px}
  .back__logo-side .brand__name{font-size:26px}
  .back__divider{width:8px;background:var(--divider)}
  .back__info{flex:1;background:linear-gradient(150deg,var(--brand-red) 0%,var(--brand-red-dark) 100%);color:var(--white);padding:46px 40px}
  .contact__name{font-size:30px;font-weight:700;letter-spacing:.5px;text-transform:uppercase}
  .contact__title{font-size:14px;letter-spacing:1.5px;text-transform:uppercase;margin:2px 0 20px}
  .contact__list{list-style:none;font-size:17px;font-weight:400}
  .contact__list li{display:flex;align-items:center;gap:12px;height:27px}
  .contact__list svg{width:16px;height:16px;flex:none}
  .contact__nmls{font-size:16px;margin-top:16px}
  .contact__web{font-size:16px;font-weight:700;margin-top:16px;letter-spacing:.5px}
</style>
</head>
<body>
  <section class="card card--front" aria-label="Card front">
    <div class="brand">
      <span class="brand__dot"></span>
      <span class="brand__name">LoanCrest Mortgage</span>
    </div>
  </section>

  <section class="card card--back" aria-label="Card back">
    <div class="back__logo-side">
      <div class="brand">
        <span class="brand__dot"></span>
        <span class="brand__name">LoanCrest Mortgage</span>
      </div>
    </div>
    <div class="back__divider"></div>
    <div class="back__info">
      <h1 class="contact__name">Dana Morrow, MBA</h1>
      <p class="contact__title">Director</p>
      <ul class="contact__list">
        <li>
          <svg viewBox="0 0 16 16" aria-hidden="true"><rect x="2" y="2" width="12" height="12" rx="1.5" fill="none" stroke="#fff" stroke-width="1.6"/></svg>
          (702) 926-1847
        </li>
        <li>
          <svg viewBox="0 0 16 16" aria-hidden="true"><path d="M4 1.5h2.5l1 3.5-1.8 1.2a8 8 0 0 0 4.1 4.1L11 8.5l3.5 1V12a2 2 0 0 1-2 2A11 11 0 0 1 2 3.5a2 2 0 0 1 2-2z" fill="#fff"/></svg>
          (702) 514-7381
        </li>
        <li>
          <svg viewBox="0 0 16 16" aria-hidden="true"><rect x="4" y="1.5" width="8" height="5" fill="#fff"/><rect x="1.5" y="6" width="13" height="6" rx="1" fill="#fff"/><rect x="4" y="10" width="8" height="4.5" fill="#fff" stroke="#c9111d" stroke-width="1"/></svg>
          (844) 637-2186
        </li>
        <li>
          <svg viewBox="0 0 16 16" aria-hidden="true"><rect x="1.5" y="2" width="13" height="12" rx="1" fill="none" stroke="#fff" stroke-width="1.6"/><path d="M4.5 8l2.5 2.5 4.5-5" fill="none" stroke="#fff" stroke-width="1.8"/></svg>
          dana.morrow@lcmhome.com
        </li>
      </ul>
      <p class="contact__nmls">NMLS # 846215</p>
      <p class="contact__web">www.lcmhome.com</p>
    </div>
  </section>
</body>
</html>
```